Custom Home Page for our new Website

We need a custom home page designed for our new website. We are a successful local copier dealer who is rebuilding our website from scratch. We have decided on Wordpress as our CMS platform and have purchased the professional Corvan theme.

The custom homepage we want will be an imitation of the screen on latest model of copiers we carry. (A picture of this is attached.) the goal is to imitate this style while creating a unique, user-friendly, helpful portal to our website.

The winning entry will make the best transition between the menu structure of our current website (www.plomra.net) and the new layout.

Target Market(s)

Our target market is small to medium sized businesses in the Southeast US. The users of our site are generally IT professionals looking for drivers/support, gatekeepers or other support staff placing service calls and supply orders or prospects looking for information about our company and products.

Requirements
Must have
• Clean design, no distracting elements
• Modern aesthetic
• A color palette that can be used as a basis for the Skin for the rest of the site (The site's look will be based on the winning homepage design.)
• Simple navigation
• Easy to read
• Easily viewed on both desktop and tablet sized screens
• Our logo
• Easily update-able
• Maximum of 4 of the large squares

```html
<!DOCTYPE html>
<html lang="en">
<head>
<meta charset="utf-8">
<title>Halden – Home</title>
<link href="https://fonts.googleapis.com/css2?family=Open+Sans:ital,wght@0,300;0,400;0,600;0,700;1,300;1,400&display=swap" rel="stylesheet">
<style>
:root{
  --red:#c0111f;
  --red-dark:#9c0a15;
  --ink:#222;
  --text:#7a7a7a;
  --rule:#dcdcdc;
  --page:#f7f7f7;
  --footer:#1b1b1b;
  --footer-text:#b9b9b9;
  --icon-grey:#6d6d6d;
}
*{box-sizing:border-box;margin:0;padding:0}
html,body{width:1164px;height:1200px;overflow:hidden}
body{position:relative;background:var(--page);font-family:"Open Sans",Arial,sans-serif;color:var(--ink)}
.abs{position:absolute}

/* header */
.nav-band{left:180px;top:48px;width:816px;height:60px;background:linear-gradient(var(--red),var(--red-dark));transform:skewX(-14deg);transform-origin:bottom left;z-index:1}
.nav-band-low{left:165px;top:100px;width:240px;height:8px;background:var(--red-dark);z-index:1}
.brand-panel{left:-20px;top:15px;width:420px;height:86px;background:#fff;transform:skewX(-8deg);box-shadow:0 2px 4px rgba(0,0,0,.12);z-index:2}
.brand{left:222px;top:36px;display:flex;align-items:center;gap:8px;font-size:34px;font-weight:700;color:#2b2b2b;letter-spacing:-1px;line-height:46px;z-index:3}
.brand-dot{width:16px;height:16px;border-radius:50%;background:var(--red)}
.nav{left:432px;top:70px;display:flex;gap:22px;font-size:13px;color:#fff;list-style:none;z-index:3}
.nav-pointer{left:443px;top:100px;width:0;height:0;border-left:6px solid transparent;border-right:6px solid transparent;border-bottom:8px solid #fff;z-index:3}
.search{left:815px;top:72px;width:155px;border-bottom:1px dashed #fff;color:#fff;font-size:12px;font-style:italic;padding:0 0 2px 12px;z-index:3}
.search svg{position:absolute;right:2px;top:1px}
.follow{left:814px;top:16px;font-size:12px;color:#666}
.social-top{left:888px;top:15px;display:flex;gap:4px}
.social-top span{width:19px;height:19px;display:block}

/* hero */
.hero{left:0;top:108px;width:1164px;height:333px;background:linear-gradient(180deg,#dcdcdc 0%,#4a4a4a 35%,#2c2c2c 70%,#3a3f5a 100%)}
.hero-cap{left:372px;top:353px;width:390px;height:88px;background:rgba(40,40,40,.55);text-align:center;color:#fff}
.hero-cap h1{font-weight:400;font-size:40px;line-height:1;margin-top:10px}
.hero-cap p{font-size:17px;margin-top:5px}

/* section headings */
.sec-title{font-size:20px;font-weight:700;color:#222}
.rule{height:2px;background:var(--rule)}
.rule i{display:block;height:3px;background:var(--red);position:relative;top:-1px}

/* achievement */
.trophy{left:166px;top:526px;width:225px;height:155px;border:2px solid #ddd;background:radial-gradient(circle at 50% 50%,#f3d37a 0%,#c99a22 30%,#222 62%,#0d0d0d 100%)}
.intro{left:405px;top:524px;width:310px;font-size:12px;line-height:16.6px;color:var(--text);font-weight:300}
.btn{left:406px;top:657px;width:104px;height:25px;background:var(--red);color:#fff;font-size:12px;font-weight:700;display:flex;align-items:center;justify-content:center;gap:8px}

/* testimonial */
.quote{left:753px;top:526px;width:252px;font-size:10.3px;line-height:15px;color:var(--text);font-style:italic;font-weight:300}
.quote-name{left:820px;top:655px;width:115px;text-align:right;font-size:12.5px;font-weight:600;color:var(--red)}
.quote-place{left:820px;top:672px;width:115px;text-align:right;font-size:10px;color:#999}
.quote-div{left:940px;top:647px;width:1px;height:44px;background:#ddd}
.avatar{left:951px;top:645px;width:44px;height:44px;border-radius:50%;border:2px solid #fff;box-shadow:0 0 0 1px #ccc;background:radial-gradient(circle,#d9b49a 0%,#6a4a3a 100%)}
.arrows{left:976px;top:489px;display:flex;gap:4px}

/* support grid */
.svc{width:250px}
.svc .ico{position:absolute;left:0;top:0;width:32px;height:32px;border-radius:50%;background:var(--icon-grey);display:flex;align-items:center;justify-content:center}
.svc .ico.on{background:var(--red)}
.svc h3{margin-left:43px;font-size:12.5px;font-weight:600;color:var(--red);letter-spacing:.2px}
.svc p{margin-left:43px;margin-top:2px;font-size:10.6px;line-height:13.5px;color:var(--text);font-weight:300}
.svc a{display:block;margin-left:43px;font-size:10.6px;color:var(--red);text-decoration:none}
.svc-sep{height:1px;background:var(--rule);width:250px}

/* footer */
.footer{left:0;top:991px;width:1164px;height:209px;background:var(--footer)}
.f-title{font-size:17px;color:#fff;font-weight:400}
.f-list{list-style:none;font-size:12.3px;color:var(--footer-text);line-height:23.3px}
.f-social{list-style:none;font-size:10.8px;color:var(--footer-text)}
.f-social li{display:flex;align-items:center;gap:10px;height:23.3px}
.f-social span{width:18px;height:18px;display:block}
.f-addr{font-size:12.3px;line-height:16px;color:var(--footer-text)}
.copy-band{left:755px;top:1131px;width:420px;height:35px;background:var(--red);transform:skewX(-20deg);transform-origin:bottom left}
.copy{left:780px;top:1141px;font-size:11px;color:#fff}
.c-fb{background:#3b5a9a}.c-tw{background:#2aa3dc}.c-gp{background:#444}.c-sk{background:#12aee8}.c-li{background:#1d7fb8}
</style>
</head>
<body>

<header>
  <div class="abs nav-band-low"></div>
  <div class="abs nav-band"></div>
  <div class="abs brand-panel"></div>
  <div class="abs brand"><span class="brand-dot"></span>Halden</div>
  <ul class="abs nav">
    <li>Home</li><li>About Us</li><li>Services</li><li>Supprot</li><li>Contact Us</li>
  </ul>
  <div class="abs nav-pointer"></div>
  <div class="abs search">Search
    <svg width="14" height="14" viewBox="0 0 14 14"><circle cx="5.5" cy="5.5" r="4" fill="none" stroke="#fff" stroke-width="1.8"/><path d="M8.5 8.5 13 13" stroke="#fff" stroke-width="2.2"/></svg>
  </div>
  <div class="abs follow">Follow Us:</div>
  <div class="abs social-top">
    <span class="c-fb"></span><span class="c-tw"></span><span class="c-gp"></span><span class="c-sk"></span><span class="c-li"></span>
  </div>
</header>

<section>
  <div class="abs hero" role="img" aria-label="Group photo of the company team in dark uniforms"></div>
  <div class="abs hero-cap">
    <h1>Join Our Team</h1>
    <p>Find out about career opportunities at Halden</p>
  </div>
</section>

<section class="achievement">
  <h2 class="abs sec-title" style="left:166px;top:478px">"IT Friendliness" Outstanding Achievement</h2>
  <div class="abs rule" style="left:166px;top:508px;width:567px"><i style="width:446px"></i></div>
  <div class="abs trophy" role="img" aria-label="Gold trophy award emblem on a black background"></div>
  <p class="abs intro">Lorem Ipsum is simply dummy text of the printing and typesetting industry. Lorem Ipsum has been the industry's standard dummy text ever since the 1500s, when an unknown printer took a galley of type and scrambled it to make a type specimen book. It has survived not only five centuries, but also the leap into electronic typesetting, remaining essentially unchanged.</p>
  <div class="abs btn">Read more
    <svg width="9" height="8" viewBox="0 0 9 8"><path d="M1 1l3 3-3 3M5 1l3 3-3 3" fill="none" stroke="#fff" stroke-width="1.2"/></svg>
  </div>
</section>

<aside class="testimonials">
  <h2 class="abs sec-title" style="left:753px;top:479px">Testimonials</h2>
  <div class="abs rule" style="left:753px;top:508px;width:244px"><i style="width:140px"></i></div>
  <div class="abs arrows">
    <svg width="8" height="10" viewBox="0 0 8 10"><path d="M6 1 2 5l4 4" fill="none" stroke="#bbb" stroke-width="1.3"/></svg>
    <svg width="8" height="10" viewBox="0 0 8 10"><path d="M2 1l4 4-4 4" fill="none" stroke="#c0111f" stroke-width="1.3"/></svg>
  </div>
  <p class="abs quote">Lorem Ipsum is simply dummy text of the printing and typesetting industry. Lorem Ipsum has been the industry's standard dummy text ever since.Lorem Ipsum is simply dummy text of the printing and typesetting industry. Lorem Ipsum has been the industry's standard dummy text ever since.</p>
  <div class="abs quote-name">Mara Ellison</div>
  <div class="abs quote-place">USA</div>
  <div class="abs quote-div"></div>
  <div class="abs avatar" role="img" aria-label="Portrait of the customer"></div>
</aside>

<section class="support">
  <div class="abs" style="left:166px;top:713px;width:20px;height:20px;border-radius:50%;border:2px solid #333"></div>
  <h2 class="abs sec-title" style="left:208px;top:709px">Supprot</h2>
  <div class="abs rule" style="left:166px;top:739px;width:831px"><i style="width:131px"></i></div>

  <div class="abs svc" style="left:166px;top:780px">
    <div class="ico on"><svg width="16" height="16" viewBox="0 0 16 16"><circle cx="8" cy="8" r="5" fill="none" stroke="#fff" stroke-width="3" stroke-dasharray="2.5 1.4"/><circle cx="8" cy="8" r="2" fill="#fff"/></svg></div>
    <h3>Remote Support</h3>
    <p>Lorem Ipsum is simply dummy text of the printing and typesetting industry. Lorem Ipsum has been.</p>
    <a>Learn more...</a>
  </div>
  <div class="abs svc" style="left:462px;top:780px">
    <div class="ico"><svg width="16" height="14" viewBox="0 0 16 14"><path d="M1 2h6v10H1zM9 2h6v10H9z" fill="#fff"/></svg></div>
    <h3>Manuals</h3>
    <p>Lorem Ipsum is simply dummy text of the printing and typesetting industry. Lorem Ipsum has been.</p>
    <a>Learn more...</a>
  </div>
  <div class="abs svc" style="left:753px;top:780px">
    <div class="ico"><svg width="16" height="16" viewBox="0 0 16 16"><path d="M3 13 13 3M3 3l10 10" stroke="#fff" stroke-width="2.4"/></svg></div>
    <h3>Troubleshooting</h3>
    <p>Lorem Ipsum is simply dummy text of the printing and typesetting industry. Lorem Ipsum has been.</p>
    <a>Learn more...</a>
  </div>

  <div class="abs svc-sep" style="left:166px;top:864px"></div>
  <div class="abs svc-sep" style="left:462px;top:864px"></div>
  <div class="abs svc-sep" style="left:753px;top:864px"></div>

  <div class="abs svc" style="left:168px;top:881px">
    <div class="ico"><svg width="14" height="16" viewBox="0 0 14 16"><path d="M2 2h7l3 3v9H2z" fill="none" stroke="#fff" stroke-width="1.6"/></svg></div>
    <h3>Brochures</h3>
    <p>Lorem Ipsum is simply dummy text of the printing and typesetting industry. Lorem Ipsum has been.</p>
    <a>Learn more...</a>
  </div>
  <div class="abs svc" style="left:462px;top:878px">
    <div class="ico"><svg width="16" height="16" viewBox="0 0 16 16"><circle cx="8" cy="8" r="6.5" fill="#fff"/><circle cx="8" cy="8" r="2.2" fill="#6d6d6d"/></svg></div>
    <h3>Drivers &amp; Software</h3>
    <p>Lorem Ipsum is simply dummy text of the printing and typesetting industry. Lorem Ipsum has been.</p>
    <a>Learn more...</a>
  </div>
  <div class="abs svc" style="left:753px;top:881px">
    <div class="ico"><svg width="16" height="16" viewBox="0 0 16 16"><path d="M8 2 13 11H3z" fill="none" stroke="#fff" stroke-width="2"/></svg></div>
    <h3>Toner Recycle</h3>
    <p>Lorem Ipsum is simply dummy text of the printing and typesetting industry. Lorem Ipsum has been.</p>
    <a>Learn more...</a>
  </div>
</section>

<footer>
  <div class="abs footer"></div>

  <h2 class="abs f-title" style="left:166px;top:1020px">Site Map</h2>
  <ul class="abs f-list" style="left:166px;top:1046px">
    <li>Home</li><li>Who We Are</li><li>What We Offer</li><li>Support</li><li>Contact Us</li>
  </ul>

  <h2 class="abs f-title" style="left:441px;top:1020px">Follow Us</h2>
  <ul class="abs f-social" style="left:441px;top:1052px">
    <li><span class="c-fb"></span>Fan us on Chatter</li>
    <li><span class="c-tw"></span>Follow us on Chirper</li>
    <li><span class="c-gp"></span>Add us to Circleup</li>
    <li><span class="c-sk"></span>Follow us on Callwave</li>
    <li><span class="c-li"></span>Join us on Workly</li>
  </ul>

  <h2 class="abs f-title" style="left:679px;top:1019px">Contact Us</h2>
  <div class="abs f-addr" style="left:680px;top:1050px">GREENVILLA<br>412 - B Alder Road<br>Greenvilla, SC 29600<br><br>864.555.0142</div>
  <div class="abs f-addr" style="left:844px;top:1049px">CHARLOTTE<br>2150 - D Pine Road<br>Charlotte, NC 28200<br><br>980.555.0187</div>

  <div class="abs copy-band"></div>
  <div class="abs copy">Copyright Norvik® 2003-13. All rights reserved</div>
</footer>

</body>
</html>
```